Multi-Faceted Legal and Finanacial Advisory Group Needs Business Card Design

We need a business card design for a newly branded Orlando Florida area advising group consisting of Attorneys, Accountants and Financial Planners. The company is named TK Counsel Partners. You will find our initial work on a business card. The information on the business card are merely guideposts and not final product. The logo does not have the be the same as provided since we have not finalized the logo. We would like to stay with a black/white/grey color scheme, but limited use of color is not out of the question.

Target Market(s)

Businesses and their Corporate Representatives

Industry/Entity Type

Business

Contact Information for Business Card

Should have Name, Title, Phone, Cell, Fax, Email and website. Logo should incorporate TK in some fashion however final logo used does not have to be the one on the document provided.

Requirements
Must have
• An TK design on front and back.

```html
<!DOCTYPE html>
<html lang="en">
<head>
<meta charset="utf-8">
<title>TK Counsel Partners — Business Card</title>
<link rel="stylesheet" href="https://fonts.googleapis.com/css2?family=Tinos&family=Raleway:wght@300;400&display=swap">
<style>
  :root {
    --backdrop-light: #e4e4e4;
    --backdrop-dark: #b9b9b9;
    --card: #2e3035;
    --frame: #9a9b9e;
    --mark: #6b6b6d;
    --white: #ffffff;
    --soft: #d8d8d8;
    --ink: #111214;
  }
  html, body {
    margin: 0;
    width: 1200px;
    height: 900px;
    overflow: hidden;
  }
  .canvas {
    position: relative;
    width: 1200px;
    height: 900px;
    background: linear-gradient(90deg, var(--backdrop-dark) 0%, var(--backdrop-light) 50%, var(--backdrop-dark) 100%);
  }
  .card {
    position: absolute;
    background: var(--card);
    border-radius: 18px;
    box-shadow: 0 2px 6px rgba(0,0,0,0.25);
  }
  .card--front { left: 319px; top: 68px; width: 588px; height: 342px; }
  .card--back  { left: 319px; top: 466px; width: 585px; height: 346px; }

  .frame-outer {
    position: absolute;
    left: 77px; top: 89px; width: 432px; height: 161px;
    border: 1px solid var(--frame);
  }
  .frame-inner {
    position: absolute;
    left: 4px; top: 4px; right: 4px; bottom: 4px;
    border: 1px solid var(--frame);
  }
  .brand-square {
    position: absolute;
    left: 117px; top: 125px; width: 94px; height: 84px;
    background: var(--mark);
  }
  .brand-name {
    position: absolute;
    left: 224px; top: 150px;
    margin: 0;
    font-family: "Tinos", "Times New Roman", serif;
    font-weight: 400;
    font-size: 28px;
    color: var(--white);
    white-space: nowrap;
  }
  .brand-tagline {
    position: absolute;
    left: 259px; top: 194px;
    margin: 0;
    font-family: "Tinos", "Times New Roman", serif;
    font-size: 9px;
    color: var(--white);
    white-space: nowrap;
  }

  .back-mark {
    position: absolute;
    left: 85px; top: 143px; width: 116px; height: 104px;
    display: flex; align-items: center; justify-content: center; gap: 10px;
    border: 1px solid var(--soft);
    box-sizing: border-box;
  }
  .back-mark__square {
    width: 30px; height: 30px;
    background: var(--mark);
  }
  .back-mark__name {
    font-family: "Tinos", "Times New Roman", serif;
    font-size: 40px;
    color: var(--white);
    line-height: 1;
  }

  .contact {
    position: absolute;
    left: 291px; top: 128px;
    font-family: "Raleway", Arial, sans-serif;
  }
  .contact__name {
    margin: 0;
    font-size: 30px;
    font-weight: 400;
    color: var(--white);
    line-height: 1;
    white-space: nowrap;
  }
  .contact__surname { font-weight: 300; color: var(--soft); }
  .contact__title {
    margin: 4px 0 0 1px;
    font-size: 15px;
    color: var(--ink);
  }
  .contact__details {
    margin: 18px 0 0 5px;
    font-size: 16px;
    font-weight: 300;
    color: var(--soft);
    line-height: 20px;
  }
</style>
</head>
<body>
<main class="canvas">
  <section class="card card--front" aria-label="Card front">
    <div class="frame-outer"><div class="frame-inner"></div></div>
    <div class="brand-square"></div>
    <h1 class="brand-name">TK Counsel Partners</h1>
    <p class="brand-tagline">Attorneys • Accountants • Financial Planners</p>
  </section>

  <section class="card card--back" aria-label="Card back">
    <div class="back-mark">
      <span class="back-mark__square"></span>
      <span class="back-mark__name">TK</span>
    </div>
    <div class="contact">
      <p class="contact__name">Daniel <span class="contact__surname">Reyes</span></p>
      <p class="contact__title">Managing Director</p>
      <p class="contact__details">hello@tkcounsel.com<br>044-555 010 246</p>
    </div>
  </section>
</main>
</body>
</html>
```